Post card

I want an educational customer postcard with our logo, email, and contact number. We are a residential foundation inspection & repair company here in Los Angeles. We provide foundation repair, earthquake retrofitting, and reinforcement.
Our number is 323-555-0148.
Email info@bramblecrestworks.com
Our license number is #2839165

OUR GOAL
Our primary objective is to empower clients with comprehensive knowledge about foundation issues and earthquake retrofitting. By educating them on the potential risks associated with foundation problems and the importance of earthquake retrofitting, we aim to equip homeowners with the necessary information to make informed decisions about safeguarding their properties. Highlighting the benefits of having their houses properly bolted not only enhances structural integrity but also provides peace of mind during seismic events, ensuring the safety and security of their homes and loved ones.

```html
<!DOCTYPE html>
<html lang="en">
<head>
<meta charset="utf-8">
<title>Bramblecrest Works – Postcard</title>
<link href="https://fonts.googleapis.com/css2?family=PT+Sans:wght@400;700&display=swap" rel="stylesheet">
<style>
  :root {
    --stage: #d6d6d6;
    --paper: #ffffff;
    --brand-blue: #3e69b4;
    --brand-blue-dark: #2b4f8f;
    --brand-red: #d02127;
    --ink: #1d1d1d;
    --photo-a: #7a6a5c;
    --photo-b: #b59a7c;
  }
  * { box-sizing: border-box; margin: 0; padding: 0; }
  html, body { width: 1200px; height: 1200px; overflow: hidden; }
  body {
    background: var(--stage);
    font-family: "PT Sans", Arial, sans-serif;
    color: var(--ink);
    position: relative;
  }
  .postcard {
    position: absolute;
    left: 239px;
    width: 720px;
    height: 515px;
    background: var(--paper);
    overflow: hidden;
  }
  .postcard--front { top: 61px; }
  .postcard--back { top: 616px; }
  .postcard__shapes { position: absolute; inset: 0; width: 720px; height: 515px; }

  .brand { position: absolute; left: 41px; top: 38px; }
  .brand__row { display: flex; align-items: center; gap: 10px; }
  .brand__mark { width: 30px; height: 30px; background: var(--brand-blue); }
  .brand__name {
    font-weight: 700; font-size: 29px; line-height: 1;
    color: var(--brand-blue); letter-spacing: 0.5px;
  }
  .brand__license {
    font-size: 9px; font-weight: 700; color: var(--ink);
    text-align: right; margin-top: 4px;
  }

  .contact-top {
    position: absolute; right: 36px; top: 36px;
    text-align: right; line-height: 1.2;
  }
  .contact-top__line { display: flex; justify-content: flex-end; align-items: center; gap: 14px; }
  .contact-top__phone { font-size: 19px; font-weight: 700; letter-spacing: 0.3px; }
  .contact-top__email { font-size: 13px; }
  .icon { width: 13px; height: 13px; flex: none; }

  .headline {
    position: absolute; color: #fff; font-weight: 700;
    font-size: 21px; line-height: 1.24; text-transform: uppercase;
  }
  .postcard--front .headline { left: 42px; top: 221px; }
  .postcard--back .headline { left: 42px; top: 248px; font-size: 21px; line-height: 1.25; }

  .photo-frame {
    position: absolute; left: 391px; top: 98px;
    width: 296px; height: 296px; border-radius: 50%;
    background: var(--paper); padding: 8px;
  }
  .photo {
    width: 100%; height: 100%; border-radius: 50%;
    background: radial-gradient(circle at 40% 40%, var(--photo-b), var(--photo-a));
  }

  .goal {
    position: absolute; left: 42px; top: 413px; width: 500px;
    color: #fff; font-size: 9.6px; line-height: 1.3;
  }

  .stamp {
    position: absolute; left: 589px; top: 43px;
    width: 95px; height: 113px; border: 1.5px solid var(--ink);
  }
  .address-line {
    position: absolute; left: 424px; width: 260px;
    border-top: 1.5px solid var(--ink);
  }

  .contact-block { position: absolute; left: 42px; top: 418px; color: #fff; }
  .contact-block__line { display: flex; align-items: center; gap: 16px; }
  .contact-block__phone { font-size: 19px; font-weight: 700; }
  .contact-block__email { font-size: 13px; margin-top: 2px; }
  .contact-block .icon { width: 17px; height: 14px; }
</style>
</head>
<body>

  <!-- Front -->
  <section class="postcard postcard--front">
    <svg class="postcard__shapes" viewBox="0 0 720 515" aria-hidden="true">
      <path d="M0 174 H720 V300 C720 420 640 500 530 515 H0 Z" fill="var(--brand-red)"/>
      <path d="M354 145 L385 174 L354 174 Z" fill="var(--brand-blue-dark)"/>
      <rect x="24" y="145" width="331" height="232" fill="var(--brand-blue)"/>
    </svg>

    <div class="brand">
      <div class="brand__row">
        <span class="brand__mark"></span>
        <span class="brand__name">BRAMBLECREST WORKS</span>
      </div>
      <div class="brand__license">#2839165</div>
    </div>

    <div class="contact-top">
      <div class="contact-top__line">
        <span class="contact-top__phone">323-555-0148</span>
        <svg class="icon" viewBox="0 0 16 16"><path d="M3 1h3l1 4-2 1.5a9 9 0 0 0 4.5 4.5L11 9l4 1v3a2 2 0 0 1-2 2C6.5 15 1 9.5 1 3a2 2 0 0 1 2-2z" fill="var(--ink)"/></svg>
      </div>
      <div class="contact-top__line">
        <span class="contact-top__email">info@bramblecrestworks.com</span>
        <svg class="icon" viewBox="0 0 16 12"><rect x="0" y="0" width="16" height="12" fill="var(--ink)"/><path d="M0 0 L8 7 L16 0" stroke="#fff" stroke-width="1.4" fill="none"/></svg>
      </div>
    </div>

    <h1 class="headline">We provide<br>foundation repair,<br>earthquake retrofitting,<br>and reinforcement.</h1>

    <div class="photo-frame">
      <div class="photo" role="img" aria-label="Photo of a worker in a hard hat and overalls holding a tablet on a construction site"></div>
    </div>

    <p class="goal">Our primary objective is to empower clients with comprehensive knowledge about foundation issues and earthquake retrofitting. By educating them on the potential risks associated with foundation problems and the importance of earthquake retrofitting, we aim to equip homeowners with the necessary information to make informed decisions about safeguarding their properties. Highlighting the benefits of having their houses properly bolted not only enhances structural integrity but also provides peace of mind during seismic events, ensuring the safety and security of their homes and loved ones.</p>
  </section>

  <!-- Back -->
  <section class="postcard postcard--back">
    <svg class="postcard__shapes" viewBox="0 0 720 515" aria-hidden="true">
      <path d="M0 260 Q0 175 110 175 H255 Q361 175 361 290 V515 H0 Z" fill="var(--brand-red)"/>
    </svg>

    <div class="brand">
      <div class="brand__row">
        <span class="brand__mark"></span>
        <span class="brand__name">BRAMBLECREST WORKS</span>
      </div>
      <div class="brand__license">#2839165</div>
    </div>

    <div class="stamp"></div>
    <div class="address-line" style="top:310px"></div>
    <div class="address-line" style="top:356px"></div>
    <div class="address-line" style="top:403px"></div>

    <h2 class="headline">We provide<br>foundation repair,<br>earthquake retrofitting,<br>and reinforcement.</h2>

    <div class="contact-block">
      <div class="contact-block__line">
        <svg class="icon" viewBox="0 0 16 16"><path d="M3 1h3l1 4-2 1.5a9 9 0 0 0 4.5 4.5L11 9l4 1v3a2 2 0 0 1-2 2C6.5 15 1 9.5 1 3a2 2 0 0 1 2-2z" fill="#fff"/></svg>
        <span class="contact-block__phone">323-555-0148</span>
      </div>
      <div class="contact-block__line">
        <svg class="icon" viewBox="0 0 16 12"><rect x="0" y="0" width="16" height="12" fill="#fff"/><path d="M0 0 L8 7 L16 0" stroke="var(--brand-red)" stroke-width="1.4" fill="none"/></svg>
        <span class="contact-block__email">info@bramblecrestworks.com</span>
      </div>
    </div>
  </section>

</body>
</html>
```